Cover page and letterhead for athlete development program

We require an exciting and dynamic cover page with a second page letterhead in a word doc format for us to use as professional stationery for letter merges and portfolio documents. We are an athlete preparation company that specialises in training up and coming sports representatives in the fitness and sports science industry. We work with athletes from ages 13 - 24 mainly. If we could have images on the cover page from the sports of:
Rugby League
Rugby Union
Hockey
Cricket
AFL
Soccer
Track and Field
Netball
Basketball
Golf
Weight training

This would be a great start. Thank you

```html
<!DOCTYPE html>
<html lang="en">
<head>
<meta charset="utf-8">
<title>Rising Stride – Letterhead and Cover</title>
<link href="https://fonts.googleapis.com/css2?family=Tinos&family=Montserrat:wght@500;700&display=swap" rel="stylesheet">
<style>
  :root {
    --backdrop: #8c979d;
    --paper: #ffffff;
    --paper-shade: #e4e4e4;
    --ink: #111111;
    --cover-black: #1d1d1d;
    --cover-deep: #0a0a0a;
    --gold: #c08a45;
    --gold-dark: #7a4a22;
    --strip-grey: #d9d9d9;
  }
  * { margin: 0; padding: 0; box-sizing: border-box; }
  html, body { width: 1200px; height: 741px; overflow: hidden; }
  body { background: var(--backdrop); position: relative; }

  .sheet { position: absolute; overflow: hidden; }

  /* Letterhead */
  .letterhead {
    left: 123px; top: 41px; width: 444px; height: 629px;
    background: linear-gradient(90deg, var(--paper-shade) 0%, #f3f3f3 55%, var(--paper) 100%);
    font-family: "Tinos", "Times New Roman", serif;
    color: var(--ink);
    font-size: 9.4px;
    line-height: 10.7px;
  }
  .brand {
    position: absolute;
    display: flex; align-items: center; gap: 6px;
    font-family: "Montserrat", Arial, sans-serif;
    font-weight: 700;
    letter-spacing: 0.5px;
  }
  .brand-square { width: 14px; height: 14px; }
  .letterhead .brand { right: 35px; top: 53px; font-size: 14px; color: var(--ink); }
  .letterhead .brand-square { background: var(--ink); }

  .letter-block { position: absolute; left: 52px; width: 340px; }
  .letter-city { top: 138px; }
  .letter-date { top: 160px; }
  .letter-recipient { top: 191px; }
  .letter-salutation { top: 256px; }
  .letter-body-1 { top: 277px; }
  .letter-body-2 { top: 389px; }
  .letter-body-3 { top: 420px; }
  .letter-closing { top: 463px; }
  .letter-signature { top: 484px; }
  .indent { padding-left: 5px; }
  .sign-name { padding-left: 18px; }

  .footer-contact, .footer-office {
    position: absolute;
    font-family: "Montserrat", Arial, sans-serif;
    font-weight: 500;
    font-size: 5px; line-height: 7px;
    text-align: right;
  }
  .footer-contact { right: 152px; top: 588px; }
  .footer-office { right: 35px; top: 580px; }
  .footer-office .office-name { font-size: 7px; letter-spacing: 2px; font-weight: 700; line-height: 9px; }

  .letter-band { position: absolute; left: 0; bottom: 0; width: 444px; height: 10px; }

  /* Cover */
  .cover {
    left: 629px; top: 42px; width: 442px; height: 624px;
    background: linear-gradient(180deg, var(--cover-black) 0%, var(--cover-deep) 100%);
  }
  .cover-top { position: absolute; left: 0; top: 0; width: 100%; height: 56px; background: linear-gradient(90deg, #f0f0f0, var(--paper)); }
  .cover .brand { left: 0; right: 0; justify-content: center; top: 181px; font-size: 17px; color: var(--paper); padding-left: 24px; }
  .cover .brand-square { background: var(--paper); width: 16px; height: 16px; }
  .cover-collage {
    position: absolute; left: 66px; top: 246px; width: 325px; height: 159px;
    background: linear-gradient(120deg, #7d5a46 0%, #a9a9a9 35%, #5a6b7d 65%, #2f5e9a 100%);
  }
  .cover-band { position: absolute; left: 0; bottom: 0; width: 442px; height: 10px; }
</style>
</head>
<body>

<section class="sheet letterhead">
  <div class="brand"><span class="brand-square"></span>RISING STRIDE</div>

  <p class="letter-block letter-city">Eastbrook, NY 10990</p>
  <p class="letter-block letter-date">June 28, 2007</p>
  <p class="letter-block letter-recipient">Ms. Dana Whitfield<br>Marlow Heritage Fellowship<br><span class="indent">48 Linden Avenue</span><br>Harbor City, NY 10950</p>
  <p class="letter-block letter-salutation">Dear Ms. Whitfield:</p>
  <p class="letter-block letter-body-1">The Marlow Heritage Fellowship has always loomed on the horizon for me. Ever since I decided to major in history, I have wanted to participate in your program. From the research that I have done, I believe that your program provides its participants with an extensively detailed look at the history of the world through hands-on experience with fossils, artifacts, and other remains that compose the blueprint of our existence. I am applying for the Marlow Heritage Fellowship because I believe that it would benefit me throughout my career and allow me to further understand the ideas behind history and how it is constructed.</p>
  <p class="letter-block letter-body-2">I believe my skills, experience, and goals make me an excellent candidate for your program.</p>
  <p class="letter-block letter-body-3">Thank you very much for considering me for the Marlow Heritage Fellowship. I am looking forward to hearing from you.</p>
  <p class="letter-block letter-closing">Sincerely,</p>
  <p class="letter-block letter-signature"><span class="sign-name">Corin</span><br>(555) 014-2290</p>

  <div class="footer-contact">Tel: (555) 301 7720 ext. 104<br>M (555) 301 7788<br>E hello@risingstride.test</div>
  <div class="footer-office"><div class="office-name">RISING STRIDE</div>Northgate Business Park<br>Calle Alameda 42, Vista Norte<br>Puerto Claro, Rep. Example</div>

  <svg class="letter-band" viewBox="0 0 444 10" aria-hidden="true">
    <polygon points="0,0 260,0 254,10 0,10" fill="#0b0b0b"/>
    <rect x="254" y="7" width="190" height="3" fill="#c08a45"/>
  </svg>
</section>

<section class="sheet cover">
  <div class="cover-top"></div>
  <div class="brand"><span class="brand-square"></span>RISING STRIDE</div>
  <div class="cover-collage" role="img" aria-label="Collage of sports photographs: rugby, hockey, cricket, crowd, basketball and soccer"></div>
  <svg class="cover-band" viewBox="0 0 442 10" aria-hidden="true">
    <polygon points="0,0 257,0 252,10 0,10" fill="#d9d9d9"/>
    <rect x="252" y="7" width="190" height="3" fill="#c08a45"/>
  </svg>
</section>

</body>
</html>
```